Landing page for Cloud Kitchen buisnies

We need a landing page design fully functional for our Cloud Kitchen company wich is based in Dubai we have a industrial kitchen setup up from where we operate our own online food brands wich are only availble for delivery

Target Market(s)

Its just a company Profile

Requirements
Must have
• Company name is Ember Plate Holdings. We have the Logo already

LOGO AND DOMAIN WE HAVE
Nice to have
• Proffesionel high quality design

```html
<!DOCTYPE html>
<html lang="en">
<head>
<meta charset="utf-8">
<title>Ember Plate Holdings</title>
<link href="https://fonts.googleapis.com/css2?family=Inter:wght@400;500;600;700;800&display=swap" rel="stylesheet">
<style>
  :root{
    --ink:#35230a;
    --gold:#a8782a;
    --gold-btn:#ad8132;
    --gold-light:#f3b84c;
    --cream:#fae9cf;
    --bar:#5a4012;
    --panel:#584014;
    --text:#5b4a35;
    --white:#ffffff;
    --photo-blue:#3f86a6;
  }
  *{box-sizing:border-box;margin:0;padding:0}
  html,body{width:1200px;height:1200px;overflow:hidden;background:var(--white);font-family:"Inter",sans-serif;color:var(--ink)}
  .page{position:absolute;left:420px;top:12px;width:588px;height:1880px;transform:scale(.625);transform-origin:0 0;background:var(--white)}
  .abs{position:absolute}
  .topbar{left:0;top:0;width:588px;height:23px;background:var(--bar);color:var(--white);font-size:7px;display:flex;align-items:center;justify-content:center}
  .brand{display:flex;align-items:center;gap:6px;font-weight:700;color:var(--gold);font-size:11px;letter-spacing:.5px;line-height:1.1}
  .brand-mark{width:18px;height:18px;border-radius:50%;background:var(--gold);flex:none}
  .nav{display:flex;font-size:7px;font-weight:600;color:var(--ink)}
  .nav a{color:inherit;text-decoration:none}
  .nav .active{color:var(--gold)}
  .cart{left:528px;top:39px;width:28px;height:28px;border-radius:5px;background:var(--gold-btn);display:flex;align-items:center;justify-content:center}
  h1,h2{font-weight:700;color:var(--ink);letter-spacing:-.2px}
  .accent{color:var(--gold)}
  .hero-title{left:32px;top:172px;font-size:27px;line-height:28px;width:250px}
  .body-text{font-size:7.5px;line-height:11px;color:var(--text)}
  .btn{display:flex;align-items:center;justify-content:center;background:var(--gold-btn);color:var(--white);font-size:7.5px;border-radius:4px;box-shadow:0 3px 4px rgba(90,60,10,.3)}
  .photo{border-radius:14px}
  .badge{background:var(--white);border-radius:7px;box-shadow:0 2px 8px rgba(0,0,0,.12);display:flex;align-items:center;justify-content:center}
  .sec-title{font-size:22px;line-height:25px}
  .step-title{font-size:8.5px;font-weight:700;color:var(--ink)}
  .step-text{font-size:7px;line-height:11px;color:var(--text);width:100px}
  .circle{border-radius:50%}
  .support-title{color:var(--white);font-size:22px;line-height:25px}
  .footer-nav{font-size:7px;font-weight:600;color:var(--ink);display:flex;gap:8px}
  .footer-nav .active{color:var(--gold)}
  .rule{left:0;top:1853px;width:588px;height:1px;background:#e8e2d8}
  .legal{font-size:5.5px;color:var(--ink)}
  .legal span{color:var(--gold)}
  .social{width:18px;height:18px;border-radius:50%;border:1px solid var(--gold)}
</style>
</head>
<body>
<div class="page">
  <div class="abs topbar">We're open and available for delivery. Order Now</div>

  <header>
    <div class="abs brand" style="left:38px;top:46px">
      <span class="brand-mark"></span>
      <span>EMBER PLATE<br>HOLDINGS</span>
    </div>
    <nav class="abs nav" style="left:359px;top:50px">
      <a class="active" style="margin-right:21px">Home</a>
      <a style="margin-right:21px">Order</a>
      <a style="margin-right:21px">Company</a>
      <a>FAQ</a>
    </nav>
    <div class="abs cart" aria-label="Cart">
      <svg width="12" height="12" viewBox="0 0 24 24" fill="none" stroke="#fff" stroke-width="2.4" stroke-linecap="round" stroke-linejoin="round"><path d="M2 3h3l2.5 12h11l2-8H6.5"/><circle cx="9" cy="20" r="1.5" fill="#fff"/><circle cx="18" cy="20" r="1.5" fill="#fff"/></svg>
    </div>
  </header>

  <section class="hero">
    <svg class="abs" style="left:0;top:0" width="588" height="400"><polygon points="256,86 588,86 588,273 330,232" fill="var(--cream)"/></svg>
    <h1 class="abs hero-title">Delicious food <span class="accent">delivered</span> to your door</h1>
    <p class="abs body-text" style="left:32px;top:266px;width:232px">Lorem Ipsum is simply dummy text of the printing and typesetting industry. Lorem Ipsum has been the industry's standard dummy text ever since the 1500.</p>
    <div class="abs btn" style="left:32px;top:307px;width:90px;height:26px">Place an Order</div>
    <div class="abs photo" role="img" aria-label="Overhead photo of shared dishes on a wooden table" style="left:301px;top:97px;width:207px;height:275px;background:linear-gradient(140deg,#5a3a22,#8a5530 45%,#b07a4a 70%,#6b4024)"></div>
    <div class="abs circle" role="img" aria-label="Hand holding a phone with the ordering app" style="left:460px;top:324px;width:80px;height:80px;background:radial-gradient(circle at 55% 45%,#38c2d8,var(--photo-blue) 60%,#2d6c8c)"></div>
    <div class="abs badge" style="left:448px;top:336px;width:28px;height:28px">
      <svg width="12" height="12" viewBox="0 0 24 24" fill="none" stroke="var(--gold)" stroke-width="2" stroke-linecap="round"><rect x="6" y="2" width="12" height="20" rx="2"/><path d="M11 18h2"/></svg>
    </div>
    <div class="abs badge" style="left:530px;top:326px;width:18px;height:18px;border-radius:5px">
      <svg width="8" height="8" viewBox="0 0 24 24" fill="none" stroke="var(--ink)" stroke-width="2.6" stroke-linecap="round"><path d="M5 13l4 4 10-10"/></svg>
    </div>
  </section>

  <section class="fresh">
    <svg class="abs" style="left:0;top:440px" width="588" height="300"><polygon points="32,28 556,13 556,291 32,291" fill="var(--cream)"/></svg>
    <h2 class="abs sec-title" style="left:76px;top:527px">The home of<br><span class="accent">fresh</span> products</h2>
    <p class="abs body-text" style="left:76px;top:594px;width:245px">Lorem Ipsum is simply dummy text of the printing and typesetting industry. Lorem Ipsum has been the industry's standard dummy text ever since the 1500.</p>
    <div class="abs btn" style="left:76px;top:640px;width:89px;height:25px">Learn About Us</div>
    <div class="abs photo" role="img" aria-label="Photo of a man enjoying a fresh meal" style="left:355px;top:492px;width:139px;height:208px;background:linear-gradient(170deg,#8a7a62,#c9b9a2 40%,#e8e0d3 70%,#9c8a6a)"></div>
    <div class="abs badge" style="left:475px;top:584px;width:40px;height:40px;border-radius:9px">
      <svg width="18" height="18" viewBox="0 0 24 24" fill="none" stroke="var(--gold)" stroke-width="1.8" stroke-linecap="round"><path d="M3 12h18a9 7 0 0 1-18 0z"/><path d="M8 12c0-3 2-5 4-5s4 2 4 5"/></svg>
    </div>
  </section>

  <section class="steps">
    <h2 class="abs" style="left:0;width:588px;text-align:center;top:778px;font-size:24px">How it works</h2>

    <div class="abs circle" role="img" aria-label="Burger and fries" style="left:53px;top:822px;width:110px;height:110px;background:radial-gradient(circle at 40% 40%,#d9a457,#b07a3a 55%,#e6e1d8)"></div>
    <div class="abs badge" style="left:123px;top:812px;width:41px;height:40px;border-radius:9px">
      <svg width="16" height="18" viewBox="0 0 20 24" fill="none" stroke="var(--ink)" stroke-width="1.8"><rect x="2" y="2" width="16" height="20" rx="1"/><path d="M6 2v20M9 8h6M9 12h6"/></svg>
    </div>
    <div class="abs step-title" style="left:68px;top:955px">Pick your menu items</div>
    <p class="abs step-text" style="left:68px;top:972px">Lorem Ipsum is simply dummy text of the printing and typesetting industry.</p>

    <div class="abs circle" role="img" aria-label="Hand holding a phone with the ordering app" style="left:240px;top:824px;width:116px;height:116px;background:radial-gradient(circle at 55% 45%,#36c4dc,var(--photo-blue) 55%,#2e6f8e)"></div>
    <div class="abs badge" style="left:223px;top:842px;width:40px;height:40px;border-radius:9px">
      <svg width="16" height="16" viewBox="0 0 24 24" fill="none" stroke="var(--gold)" stroke-width="2" stroke-linecap="round"><rect x="6" y="2" width="12" height="20" rx="2"/><path d="M11 18h2"/></svg>
    </div>
    <div class="abs badge" style="left:338px;top:832px;width:22px;height:22px;border-radius:6px">
      <svg width="10" height="10" viewBox="0 0 24 24" fill="none" stroke="var(--ink)" stroke-width="2.6" stroke-linecap="round"><path d="M5 13l4 4 10-10"/></svg>
    </div>
    <div class="abs step-title" style="left:256px;top:955px">Place your order</div>
    <p class="abs step-text" style="left:249px;top:972px">Lorem Ipsum is simply dummy text of the printing and typesetting industry.</p>

    <div class="abs circle" role="img" aria-label="House with a green lawn" style="left:419px;top:816px;width:112px;height:112px;background:linear-gradient(180deg,#9aa3ad,#5d5a5a 50%,#4c7a2a)"></div>
    <div class="abs circle" role="img" aria-label="Customer avatar" style="left:409px;top:814px;width:42px;height:42px;background:#d8c7b4;border:3px solid #fff;box-shadow:0 2px 6px rgba(0,0,0,.15)"></div>
    <div class="abs circle" role="img" aria-label="Courier avatar" style="left:508px;top:855px;width:34px;height:34px;background:#e7b9a0;border:3px solid #fff;box-shadow:0 2px 6px rgba(0,0,0,.15)"></div>
    <div class="abs step-title" style="left:411px;top:955px">Your order will be delivered</div>
    <p class="abs step-text" style="left:416px;top:972px">Lorem Ipsum is simply dummy text of the printing and typesetting industry.</p>
  </section>

  <section class="checkout">
    <svg class="abs" style="left:0;top:1050px" width="588" height="290"><polygon points="35,24 559,8 559,286 35,286" fill="var(--cream)"/></svg>
    <div class="abs" role="img" aria-label="Two phones showing the ordering app screens" style="left:78px;top:1095px;width:165px;height:225px;border-radius:16px;background:linear-gradient(150deg,#2a2a2a,#e9eef2 20%,#ffffff 55%,#dfe4e8 85%,#2a2a2a)"></div>
    <h2 class="abs sec-title" style="left:294px;top:1132px">Order online with our<br><span class="accent">simple</span> checkout</h2>
    <p class="abs body-text" style="left:294px;top:1196px;width:245px">Lorem Ipsum is simply dummy text of the printing and typesetting industry. Lorem Ipsum has been the industry's standard dummy text ever since the 1500.</p>
    <div class="abs btn" style="left:294px;top:1237px;width:90px;height:26px">Place an Order</div>
  </section>

  <section class="support">
    <div class="abs" role="img" aria-label="Overhead photo of a table full of dishes" style="left:32px;top:1383px;width:255px;height:338px;background:linear-gradient(160deg,#6e3f22,#a9774a 40%,#d7c2a6 60%,#7b4a28)"></div>
    <div class="abs" style="left:301px;top:1383px;width:255px;height:338px;background:var(--panel)"></div>
    <h2 class="abs support-title" style="left:345px;top:1476px"><span style="color:var(--gold-light)">Support</span> good<br>food<br>and local<br>business</h2>
    <div class="abs btn" style="left:345px;top:1599px;width:90px;height:26px;background:var(--gold-light);color:var(--ink);box-shadow:none">Order Now</div>
  </section>

  <footer>
    <div class="abs brand" style="left:32px;top:1796px">
      <span class="brand-mark"></span>
      <span>EMBER PLATE<br>HOLDINGS</span>
    </div>
    <nav class="abs footer-nav" style="left:396px;top:1803px">
      <span class="active">Home</span><span>|</span><span>Order</span><span>|</span><span>Company</span><span>|</span><span>FAQ</span>
    </nav>
    <div class="abs rule"></div>
    <p class="abs legal" style="left:32px;top:1867px">© 2020 Ember Plate Holdings. All Rights Reserved. <span>Terms</span> &amp; <span>Privacy Policy</span></p>
    <div class="abs social" aria-label="Social link" style="left:484px;top:1860px"></div>
    <div class="abs social" aria-label="Social link" style="left:511px;top:1860px"></div>
    <div class="abs social" aria-label="Social link" style="left:538px;top:1860px"></div>
  </footer>
</div>
</body>
</html>
```